Government Contracting business needs a website design.

Pemberton & Quill, LLC is a minority owned Service Disabled Veteran Owned Small Business (SDVOSB) that provides Strategic Planning, Public Health Emergency Response, and Data Management Solutions for Federal Civilian and Defense Agencies. We have over 20 years of experience helping health and defense agencies develop concept of operations, deploy assets and personnel in Hot Zones around the world, and deliver goods and services all of the globe.

We are a leader in the field of Data Management. We help our customers develop cloud migration and disaster recovery strategies. We are experts with database management, data replication, queries, consolidation, and records management.

We are looking for a very nice and simple website designs that states clearly what we do as a company and that is easy for our customers to follow. We would like to have some moving pictures that are base on our expertise. We want the website to be easy to use and have the scroll down features that keeps things all on the same page when clicking on the menu. I attached a document with what we need on the website. I will also attach our logo. We want it to look simple clean and very professional.

Target Market(s)

Government Contracting, Management Consulting, Health

Industry/Entity Type

Government

Coding

Coded - Design and coding required

Number of Pages Required

1 page

Font styles to use
Serif

Requirements
Must have
• Very nice picture slides that speaks to our capabilities in Disaster Response, Strategic Planning, and Database Management. Slick look and design. Make sure SDVOSB Logo is right at the beginning of website as our customers is looking for that certification. Very nice colors that blend well with our logo.
Nice to have
• Very nice and slick colors that blends well with logo.
Should not have
• Basic website design that are weary on the eye. No bright colors, just simple colors that looks good with logo.

```html
<!DOCTYPE html>
<html lang="en">
<head>
<meta charset="utf-8">
<title>Pemberton &amp; Quill, LLC</title>
<link href="https://fonts.googleapis.com/css2?family=Roboto+Slab:wght@400;700;900&family=Open+Sans:wght@400;600;700&display=swap" rel="stylesheet">
<style>
:root{
  --red:#b8141b;
  --red-dark:#8f0f14;
  --navy:#0e3d7c;
  --blue:#1a5bb0;
  --ink:#222;
  --text:#666;
  --muted:#999;
  --light:#f2f2f2;
  --line:#e2e2e2;
  --dark:#1d1d1d;
  --white:#fff;
}
*{margin:0;padding:0;box-sizing:border-box}
html,body{width:1200px;height:3184px;overflow:hidden}
body{font-family:"Open Sans",Arial,sans-serif;color:var(--text);background:var(--white);font-size:14px;line-height:1.6}
h1,h2,h3,h4{font-family:"Roboto Slab",Georgia,serif;color:var(--ink)}
.wrap{width:960px;margin:0 auto;position:relative}
.photo{display:block}

/* top bar */
.topbar{height:24px;background:var(--red-dark);color:#f3d0d1;font-size:11px}
.topbar .wrap{display:flex;justify-content:space-between;align-items:center;height:24px}
.topbar span{margin-left:18px}

/* header */
.header{height:104px;background:var(--white);border-bottom:1px solid var(--line)}
.header .wrap{display:flex;justify-content:space-between;align-items:center;height:104px}
.brand{display:flex;align-items:center;gap:12px;font-family:"Roboto Slab",serif;font-weight:700;color:var(--navy);font-size:18px}
.brand i{width:64px;height:64px;border-radius:50%;background:var(--navy);display:block}
.nav{display:flex;gap:26px;font-size:12px;font-weight:600;text-transform:uppercase;color:var(--ink)}
.nav .active{color:var(--red)}

/* hero */
.hero{height:492px;position:relative;background:linear-gradient(100deg,#e9e7e3 0%,#d9cfc2 45%,#c9a98a 75%,#b08866 100%)}
.hero-copy{position:absolute;left:120px;top:120px;width:520px}
.hero h1{font-size:58px;font-weight:900;color:var(--red);line-height:1.05}
.hero .tag{font-family:"Roboto Slab",serif;font-weight:700;font-size:15px;color:var(--ink);margin:6px 0 14px}
.hero p{font-size:13px;color:#444;margin-bottom:40px}
.btn{display:inline-block;height:42px;line-height:42px;padding:0 24px;font-size:12px;font-weight:700;color:var(--white);text-transform:uppercase;margin-right:10px}
.btn-dark{background:var(--dark)}
.btn-blue{background:var(--blue)}

/* services */
.services{height:240px;padding-top:40px}
.services .wrap{display:flex;justify-content:space-between}
.service{width:225px;position:relative}
.service .icon{position:absolute;left:92px;top:-30px;width:42px;height:42px;border-radius:50%;background:var(--white);border:2px solid var(--line);display:flex;align-items:center;justify-content:center;z-index:2}
.service .photo{height:140px}
.service .label{height:30px;background:var(--red);color:var(--white);font-size:12px;font-weight:600;text-align:center;line-height:30px}

/* welcome */
.welcome{height:420px;padding-top:20px}
.welcome .wrap{display:flex;justify-content:space-between}
.welcome-copy{width:500px}
.welcome h2{font-size:28px;font-weight:900;margin-bottom:16px}
.welcome p{font-size:13px;margin-bottom:14px}
.contact{display:flex;align-items:center;gap:14px;margin-top:18px;font-size:12px}
.contact .sq{width:40px;height:40px;background:#444;display:flex;align-items:center;justify-content:center;flex:none}
.contact b{color:var(--ink);display:block;font-size:13px}
.welcome .photo{width:300px;height:300px;margin-top:20px;border:6px solid var(--light)}

/* why */
.why{height:320px;background:var(--navy);color:#d6e2f2;position:relative;margin-top:40px}
.appointment{position:absolute;left:180px;top:-30px;width:240px;height:370px;background:var(--red);padding:22px 24px}
.appointment h3{color:var(--white);font-size:17px;font-weight:700;margin-bottom:16px;text-transform:uppercase}
.field{height:30px;background:var(--white);margin-bottom:10px;font-size:11px;line-height:30px;padding-left:10px;color:var(--muted)}
.field.tall{height:60px}
.submit{display:inline-block;background:var(--dark);color:var(--white);font-size:11px;font-weight:700;padding:6px 16px}
.why-copy{position:absolute;left:480px;top:50px;width:600px}
.why h2{color:var(--white);font-size:34px;font-weight:900;margin-bottom:14px}
.why p{font-size:12.5px;margin-bottom:12px}

/* team */
.section-title{text-align:center;font-size:30px;font-weight:900;padding-top:40px}
.section-title:after{content:"";display:block;width:60px;height:3px;background:var(--red);margin:10px auto 0}
.team{height:440px}
.team .wrap{display:flex;justify-content:space-between;margin-top:40px}
.member{width:465px;height:250px;border:1px solid var(--line);display:flex;padding:20px;gap:20px}
.member .photo{width:170px;height:208px;flex:none}
.member h4{font-size:17px;font-weight:700}
.member .role{font-size:12px;color:var(--red);margin-bottom:10px}
.member p{font-size:12px;margin-bottom:14px}
.more{display:inline-block;border:1px solid #bbb;font-size:10px;font-weight:700;padding:3px 10px;color:var(--ink)}

/* blog */
.blog{height:480px}
.blog .wrap{display:flex;justify-content:space-between;margin-top:40px}
.blog-feature{width:440px;height:340px;position:relative}
.blog-feature .photo{height:340px}
.date{position:absolute;left:16px;bottom:16px;width:54px;height:54px;background:var(--red);color:var(--white);font-family:"Roboto Slab",serif;text-align:center;font-size:20px;font-weight:700;line-height:1;padding-top:8px}
.date small{display:block;font-size:10px;font-weight:400;margin-top:4px}
.posts{width:490px}
.post{display:flex;gap:18px;margin-bottom:30px}
.post .thumb{width:150px;height:150px;position:relative;flex:none}
.post .thumb .photo{height:150px}
.post .date{left:0;bottom:0}
.post h4{font-size:15px;font-weight:700;color:var(--red)}
.post .meta{font-size:11px;color:var(--muted);margin-bottom:6px}
.post p{font-size:12px;margin-bottom:10px}
.post .foot{display:flex;justify-content:space-between;align-items:center;font-size:11px;color:var(--muted)}

/* consulting */
.consult{height:140px;background:var(--light);margin-top:0}
.consult .wrap{display:flex;justify-content:space-between;align-items:center;height:140px}
.consult h3{font-size:22px;font-weight:900}
.consult p{font-size:12px}
.consult .btn{height:48px;line-height:48px;padding:0 30px}

/* newsletter */
.newsletter{height:200px;background:var(--red);text-align:center;color:#f6d4d5;padding-top:30px}
.newsletter h2{color:var(--white);font-size:32px;font-weight:900;letter-spacing:1px}
.newsletter p{font-size:12px;margin-bottom:16px}
.signup{display:inline-flex}
.signup .input{width:330px;height:38px;background:var(--white);font-size:12px;line-height:38px;text-align:left;padding-left:12px;color:var(--muted)}
.signup .go{height:38px;line-height:38px;padding:0 22px;background:var(--dark);color:var(--white);font-size:12px;font-weight:700}

/* footer */
.footer{height:244px;background:var(--dark);text-align:center;color:#aaa}
.footer h2{color:var(--white);font-size:40px;font-weight:400;padding-top:26px}
.social{display:flex;justify-content:center;gap:14px;margin:16px 0 30px}
.social i{width:34px;height:34px;border-radius:50%;border:1px solid #777;display:block}
.footnav{display:flex;justify-content:center;gap:36px;font-size:12px;text-transform:uppercase;color:#ccc;border-top:1px solid #333;padding-top:16px}
.copy{font-size:11px;margin-top:12px;color:#888}
</style>
</head>
<body>

<div class="topbar"><div class="wrap"><div>☎ (703) 555-0192 &nbsp; ✉ contact@pembertonquill.com</div><div><span>Login</span><span>Register</span><span>Search</span></div></div></div>

<header class="header"><div class="wrap">
  <div class="brand"><i></i>Pemberton &amp; Quill, LLC</div>
  <nav class="nav"><span class="active">Home</span><span>About Us</span><span>Team</span><span>Core Capabilities</span><span>Our Services</span><span>Contact Us</span></nav>
</div></header>

<section class="hero" role="img" aria-label="Smiling senior couple embracing, warm background">
  <div class="hero-copy">
    <h1>MISSION ORIENTED</h1>
    <div class="tag">HEALTH IT AND ACQUISITION FOR THE DEFENSE AND VA COMMUNITY</div>
    <p>We are a Service Disabled Veteran Owned Small Business (SDVOSB) specializing in Defense Health IT for the defense and VA community.</p>
    <span class="btn btn-dark">Read More</span><span class="btn btn-blue">Ask Quote</span>
  </div>
</section>

<section class="services"><div class="wrap">
  <div class="service"><div class="icon"><svg width="20" height="20" viewBox="0 0 20 20"><rect x="3" y="10" width="3" height="7" fill="#666"/><rect x="8" y="6" width="3" height="11" fill="#666"/><rect x="13" y="3" width="3" height="14" fill="#666"/></svg></div><div class="photo" role="img" aria-label="Team planning around a table" style="background:linear-gradient(135deg,#c8c2b8,#8a7d70)"></div><div class="label">Strategic Planning</div></div>
  <div class="service"><div class="icon"><svg width="20" height="20" viewBox="0 0 20 20"><rect x="8" y="3" width="4" height="14" fill="#666"/><rect x="3" y="8" width="14" height="4" fill="#666"/></svg></div><div class="photo" role="img" aria-label="Health responders at work" style="background:linear-gradient(135deg,#d7dde4,#7f93a8)"></div><div class="label">Public Health Emergency Response</div></div>
  <div class="service"><div class="icon"><svg width="20" height="20" viewBox="0 0 20 20"><ellipse cx="10" cy="5" rx="6" ry="2.5" fill="#666"/><rect x="4" y="5" width="12" height="10" fill="#666"/><ellipse cx="10" cy="15" rx="6" ry="2.5" fill="#666"/></svg></div><div class="photo" role="img" aria-label="Data management on a screen" style="background:linear-gradient(135deg,#b9c6d6,#3f5f85)"></div><div class="label">Data Management Solution</div></div>
  <div class="service"><div class="icon"><svg width="20" height="20" viewBox="0 0 20 20"><rect x="4" y="2" width="12" height="16" fill="none" stroke="#666" stroke-width="2"/><rect x="7" y="6" width="6" height="2" fill="#666"/><rect x="7" y="11" width="6" height="2" fill="#666"/></svg></div><div class="photo" role="img" aria-label="Government building exterior" style="background:linear-gradient(135deg,#e2e2e0,#9a9c9e)"></div><div class="label">Contracts Vehicles</div></div>
</div></section>

<section class="welcome"><div class="wrap">
  <div class="welcome-copy">
    <h2>WELCOME TO SDVOSB</h2>
    <p>Pemberton &amp; Quill, LLC is a minority owned Service Disabled Veteran Owned Small Business (SDVOSB) that provides Strategic Planning, Public Health Emergency Response, and Data Management Solutions for Federal Civilian and Defense Agencies. We have over 20 years of experience helping health and defense agencies develop concept of operations, deploy assets and personnel in Hot Zones around the world, and deliver goods and services all of the globe.</p>
    <p>We are a leader in the field of Data Management. We help our customers develop cloud migration and disaster recovery strategies. We are experts with database management, data replication, queries, consolidation, and records management.</p>
    <div class="contact"><div class="sq"><svg width="18" height="14" viewBox="0 0 18 14"><rect x="1" y="1" width="16" height="12" fill="none" stroke="#fff" stroke-width="1.6"/><path d="M1 1l8 7 8-7" fill="none" stroke="#fff" stroke-width="1.6"/></svg></div><div><b>contact@pembertonquill.com</b>You will be replied to within 24 hours, Monday through Friday.</div></div>
    <div class="contact"><div class="sq"><svg width="16" height="16" viewBox="0 0 16 16"><path d="M3 1l3 3-2 2c1 2 3 4 5 5l2-2 3 3-2 3C7 15 1 9 1 3z" fill="#fff"/></svg></div><div><b>(703) 555-0192</b>Call our office number and you will reach our team.</div></div>
  </div>
  <div class="photo" role="img" aria-label="Business professionals in an office" style="background:linear-gradient(135deg,#eef0f3,#aab3bf)"></div>
</div></section>

<section class="why">
  <div class="appointment">
    <h3>Make an Appointment</h3>
    <div class="field">First Name</div><div class="field">Last Name</div><div class="field">Phone Number</div><div class="field">Email</div><div class="field tall">Message</div>
    <span class="submit">SUBMIT</span>
  </div>
  <div class="why-copy">
    <h2>WHY HIRE US?</h2>
    <p>Our team brings decades of field experience to every engagement. We plan carefully, respond quickly and deliver on schedule for agencies that cannot afford delays. From concept of operations to final delivery, we stay accountable to clear goals and measurable outcomes, and we keep our clients informed at each step of the work.</p>
    <p>We combine public health knowledge with strong data practice. Our specialists design secure systems, migrate records to the cloud and build recovery plans that hold up under pressure. Agencies rely on us because we listen first, act with care and treat every mission as our own, whether at home or in the field abroad.</p>
  </div>
</section>

<section class="team">
  <h2 class="section-title">OUR TEAM</h2>
  <div class="wrap">
    <div class="member"><div class="photo" role="img" aria-label="Portrait of team member" style="background:linear-gradient(160deg,#ddd6cf,#8d7f74)"></div><div><h4>Ret. SFC Marcus D. Ellery</h4><div class="role">Chief Executive Officer</div><p>Marcus leads the firm with over twenty years of service in defense health operations. He guides strategy, partnerships and field response, and keeps every program focused on mission results for our agency clients.</p><span class="more">READ MORE</span></div></div>
    <div class="member"><div class="photo" role="img" aria-label="Portrait of team member" style="background:linear-gradient(160deg,#d9d9d9,#7b7b7b)"></div><div><h4>Mr. Colin T. Avery</h4><div class="role">Director of Data Management</div><p>Colin directs our data practice, overseeing cloud migration, database consolidation and records management. He helps agencies build recovery plans and reliable systems that keep critical information safe.</p><span class="more">READ MORE</span></div></div>
  </div>
</section>

<section class="blog">
  <h2 class="section-title">LATEST BLOG</h2>
  <div class="wrap">
    <div class="blog-feature"><div class="photo" role="img" aria-label="Colleagues reviewing documents together" style="background:linear-gradient(135deg,#f0ece6,#b9a995)"></div><div class="date">18<small>JUN</small></div></div>
    <div class="posts">
      <div class="post"><div class="thumb"><div class="photo" role="img" aria-label="Business meeting" style="background:linear-gradient(135deg,#e6e1da,#a3978a)"></div><div class="date">16<small>JUN</small></div></div><div><h4>BLOG HEADING HERE</h4><div class="meta">June 16, 2017 · Admin</div><p>A short update on recent work with our agency partners in planning and emergency response programs.</p><div class="foot"><span class="more">READ MORE</span><span>3 Likes · 2 Comments</span></div></div></div>
      <div class="post"><div class="thumb"><div class="photo" role="img" aria-label="Professional at a desk" style="background:linear-gradient(135deg,#e8ebe2,#9ca58c)"></div><div class="date">12<small>JUN</small></div></div><div><h4>BLOG HEADING HERE</h4><div class="meta">June 12, 2017 · Admin</div><p>Notes on cloud migration and disaster recovery practice for federal civilian and defense teams.</p><div class="foot"><span class="more">READ MORE</span><span>5 Likes · 1 Comment</span></div></div></div>
    </div>
  </div>
</section>

<section class="consult"><div class="wrap">
  <div><h3>CONSULTING SERVICE</h3><p>Talk with our specialists about planning, response and data needs for your agency.</p></div>
  <span class="btn btn-dark">Get Free Consultation ›</span>
</div></section>

<section class="newsletter">
  <h2>NEWSLETTER</h2>
  <p>Enter your email address for getting updates</p>
  <div class="signup"><div class="input">Enter your email</div><div class="go">Subscribe</div></div>
</section>

<footer class="footer">
  <h2>Join the conversation</h2>
  <div class="social"><i></i><i></i><i></i><i></i><i></i></div>
  <div class="footnav"><span>Home</span><span>About Us</span><span>Team</span><span>Core Capabilities</span><span>Our Services</span><span>Contact Us</span></div>
  <div class="copy">© 2017 Pemberton &amp; Quill, LLC. All rights reserved.</div>
</footer>

</body>
</html>
```